Flyer Lieferservice / Gutschein / Visitenkarte
Zielgruppe
Restaurant
Aufgabenstellung
Wir benötigen:
Lieferservice Flyer mit Speisekarte
Gutschein Flyer
Visitenkarten
Farbe: Schwarz & Gold siehe Website
Speisekarte: (siehe Anhang)
Wichtige Inhalte:
Speiskarte
Social Media
Anschrift
Telefonnummer
Website
App Verweis
(bishergie Flyer zur Ansicht im Anhang)

```html
<!DOCTYPE html>
<html lang="de">
<head>
<meta charset="utf-8">
<title>Restaurant Zum Sonnenkorb – Lieferservice Flyer</title>
<link href="https://fonts.googleapis.com/css2?family=Poppins:wght@400;500;600&display=swap" rel="stylesheet">
<style>
  :root {
    --page-bg: #c9c7c6;
    --black: #0b0b0b;
    --slate: #1c1c1c;
    --gold: #c9a934;
    --gold-text: #d4b32f;
    --pill-grey: #5e5e58;
    --white: #ffffff;
    --paper: #f1f1f1;
    --ink: #4a4a48;
    --line: #555555;
  }
  * { margin: 0; padding: 0; box-sizing: border-box; }
  html, body { width: 1200px; height: 864px; overflow: hidden; }
  body {
    background: var(--page-bg);
    font-family: "Poppins", Arial, sans-serif;
    display: flex; align-items: center; justify-content: center;
  }
  .flyer {
    position: relative;
    width: 580px; height: 820px;
    background: var(--paper);
    overflow: hidden;
    box-shadow: 0 10px 30px rgba(0,0,0,.25);
  }
  .hero {
    position: absolute; left: 0; top: 0; width: 580px; height: 565px;
    background:
      radial-gradient(ellipse 200px 170px at 330px 430px, #b8321c 0%, #8a2413 45%, rgba(30,20,18,0) 100%),
      radial-gradient(ellipse 190px 150px at 480px 210px, #555 0%, rgba(40,40,40,0) 100%),
      linear-gradient(160deg, #0a0a0a 0%, var(--slate) 60%, #121212 100%);
  }
  .frame {
    position: absolute; left: 18px; top: 18px; width: 544px; height: 580px;
    border: 2px solid var(--white);
    pointer-events: none;
  }
  .brand {
    position: absolute; left: 0; top: 52px; width: 580px; text-align: center;
  }
  .brand-mark {
    width: 46px; height: 46px; border-radius: 50%;
    background: var(--gold); margin: 0 auto 18px;
  }
  .brand-name {
    color: var(--gold-text); font-size: 30px; font-weight: 500; letter-spacing: .5px;
  }
  .brand-web {
    color: var(--white); font-size: 12px; margin-top: 4px; letter-spacing: .3px;
  }
  .order-pill {
    position: absolute; left: 34px; top: 498px; width: 512px; height: 50px;
    border-radius: 25px; overflow: hidden; display: flex;
  }
  .order-label {
    flex: 0 0 220px; background: var(--pill-grey); color: var(--white);
    font-size: 20px; font-weight: 600; display: flex; align-items: center; justify-content: center;
  }
  .order-phone {
    flex: 1; background: var(--gold); color: var(--white);
    font-size: 26px; font-weight: 600; display: flex; align-items: center; justify-content: center; letter-spacing: 1px;
  }
  .info {
    position: absolute; left: 0; top: 565px; width: 580px; height: 255px; text-align: center;
  }
  .app-title {
    margin-top: 24px; color: var(--ink); font-size: 24px; font-weight: 500; letter-spacing: .5px;
  }
  .store-badges { display: flex; justify-content: center; gap: 18px; margin-top: 16px; }
  .store-badge { width: 120px; height: 36px; border-radius: 6px; background: #111; }
  .divider { width: 440px; height: 1px; background: var(--line); margin: 26px auto 16px; }
  .details { color: var(--gold-text); font-size: 10.5px; line-height: 1.6; padding: 0 50px; }
  .details strong { font-weight: 600; }
</style>
</head>
<body>
  <article class="flyer">
    <div class="hero" role="img" aria-label="Foto: Teller Bandnudeln mit Tomatensauce auf dunklem Schiefer, grobes Stricktuch und Kirschtomaten"></div>
    <div class="frame"></div>

    <header class="brand">
      <div class="brand-mark"></div>
      <div class="brand-name">Restaurant Zum Sonnenkorb</div>
      <div class="brand-web">www.restaurantzumsonnenkorb.de</div>
    </header>

    <div class="order-pill">
      <div class="order-label">BESTELLE UNTER</div>
      <div class="order-phone">04321 | 5550172</div>
    </div>

    <section class="info">
      <h2 class="app-title">LIEFERSHOP - JETZT AUCH ALS APP</h2>
      <div class="store-badges">
        <div class="store-badge" aria-label="App-Badge"></div>
        <div class="store-badge" aria-label="App-Badge"></div>
      </div>
      <div class="divider"></div>
      <p class="details">
        <strong>Öffnungszeiten:</strong> Mittwoch - Samstag von 17 Uhr bis 21:30 | Sonn- und Feiertag von 11 Uhr bis 21:30 Uhr<br>
        <strong>Liefergebiete:</strong> Lindenau-Hochfeld | Dettwiesen | Eichstein-Leonhafen | Grabenau-Neuhof |
        Stillensee | Karlsau-Neuhardt | Neuwiesen bzw. PLZ 79999
      </p>
    </section>
  </article>
</body>
</html>
```